Advertising flyer for proofreading business.

Hello everyone,

I need an advertising flyer for a new proofreading company in Australia.

I would like your design in be in two sizes:
- A4 (to be posted on noticeboards),
- A6 (to be printed in larger quantity to give away)
(please see the size specification file attached).

The text file is attached (Ad Text) and it contains lots of information. Please feel free to include your choice of text from the text file, but please include Poster title, and highlight 'ESL' and students discounts.

I understand that it is impossible to include the same amount of information on A6 and A4, so please feel free to chose what fits on each of them, but please keep the design similar.

I have attached our company logo, but feel free to adjust it to the poster design (feel free to change the color as well). The original logo file contains circle around it, please feel free to remove it and include only the typeset as it can be seen here: http://www.lexmarka.com.au/.

Flyers will be printed, so please see the specification file for details.

I will do my best to respond to feedback as soon as possible.

I appreciate your participation, time and help,
Best wishes,
Bartosz

Target Market(s)

Students, authors

Industry/Entity Type

Business

Colors

Designer to choose colors to be used in the design.

Requirements
Must have
• It would be good if poster is easy to spot on busy noticeboards and attract attention.
• Please keep the poster in the positive/optimistic mood, and so that it focuses on students, maybe photos of graduates(?).
• Poster title,
• Please include the list of proof-read documents as they are described in the attached text file (Ad Text).
• Please highlight students discounts and ESL.
Nice to have
• I would like to leave the creative freedom to all designers so at this point I have not adjusted the Look and Feel sliders. Please feel free to offer your own take on this.
• It would be nice if most of the text could be fit to the poster.

```html
<!DOCTYPE html>
<html lang="en">
<head>
<meta charset="utf-8">
<title>Clearpage – Proofreading Flyer</title>
<link href="https://fonts.googleapis.com/css2?family=Bebas+Neue&family=Lato:ital,wght@0,400;0,700;0,900;1,400&display=swap" rel="stylesheet">
<style>
  :root{
    --teal:#22c3a6;
    --teal-dark:#159a83;
    --teal-deep:#0f7e6b;
    --ink:#2a2a2a;
    --paper:#f6f6f6;
    --footer:#262626;
    --stage:#d9d9d9;
    --white:#ffffff;
  }
  *{margin:0;padding:0;box-sizing:border-box}
  html,body{width:1200px;height:1000px;overflow:hidden;background:var(--stage)}
  body{font-family:'Lato',sans-serif;color:var(--ink);position:relative}
  .flyer{position:absolute;left:270px;top:33px;width:660px;height:934px;background:var(--paper);overflow:hidden;box-shadow:0 6px 24px rgba(0,0,0,.18)}
  .header-shape{position:absolute;left:0;top:0;width:660px;height:400px}
  .hero-photo{position:absolute;right:0;top:0;width:300px;height:380px;background:linear-gradient(160deg,#39d2b6 0%,#1aa88f 55%,#128a75 100%);clip-path:polygon(12% 0,100% 0,100% 100%,0 78%)}
  .headline{position:absolute;left:40px;top:34px;width:420px;color:var(--white)}
  .headline h1{font-family:'Bebas Neue',sans-serif;font-weight:400;font-size:54px;line-height:.9;letter-spacing:.5px}
  .headline .lead{font-weight:900;font-size:16px;line-height:1.25;margin-top:18px}
  .headline .detail{font-size:13px;line-height:1.3;margin-top:10px;width:330px}
  .brand{position:absolute;left:270px;top:278px;width:120px;height:120px;border-radius:50%;background:var(--teal);border:5px solid var(--white);display:flex;align-items:center;justify-content:center;box-shadow:0 3px 8px rgba(0,0,0,.2)}
  .brand span{font-family:'Lato',sans-serif;font-weight:700;font-size:20px;color:var(--white)}
  .section-title{font-family:'Bebas Neue',sans-serif;font-weight:400;color:var(--teal);font-size:32px;line-height:1}
  .services{position:absolute;left:40px;top:412px;width:300px}
  .services ul{list-style:none;margin-top:10px}
  .services li{font-size:15px;line-height:1.3;padding-left:18px;position:relative;font-weight:700}
  .services li::before{content:"";position:absolute;left:0;top:6px;width:8px;height:8px;background:var(--teal)}
  .services li.cont::before{display:none}
  .price-guide{position:absolute;left:350px;top:448px;width:280px;font-size:13px;line-height:1.3}
  .price-guide .section-title{margin-bottom:10px}
  .price-guide p{margin-bottom:9px}
  .price-guide .hl{color:var(--teal);font-weight:900}
  .price-guide small{font-size:10.5px}
  .desk-photo{position:absolute;left:40px;top:705px;width:270px;height:150px;background:linear-gradient(135deg,#c9b59a 0%,#e8e4dc 45%,#7d8a94 100%)}
  .testimonial{position:absolute;left:335px;top:728px;width:290px;height:130px;border:1px solid var(--teal);padding:22px 14px 10px}
  .testimonial .section-title{position:absolute;left:12px;top:-16px;background:var(--paper);padding:0 6px;font-size:28px}
  .testimonial blockquote{font-size:10.5px;line-height:1.35}
  .testimonial .by{margin-top:10px;text-align:right;font-size:9.5px;line-height:1.3;border-top:1px solid #999;padding-top:4px;margin-left:140px}
  .testimonial .by strong{display:block}
  .footer{position:absolute;left:0;bottom:0;width:660px;height:48px;background:var(--footer);color:var(--white);display:flex;align-items:center;justify-content:center;font-size:15px;font-weight:700}
</style>
</head>
<body>
  <main class="flyer">
    <svg class="header-shape" viewBox="0 0 660 400" aria-hidden="true">
      <path d="M0 0H660V392C560 330 470 300 330 300C200 300 90 330 0 372Z" fill="var(--teal-deep)"/>
      <path d="M0 0H660V378C560 318 470 288 330 288C200 288 90 318 0 358Z" fill="var(--teal)"/>
    </svg>
    <div class="hero-photo" role="img" aria-label="Photo of a young man with glasses at a desk, tinted teal"></div>

    <header class="headline">
      <h1>Help with English<br>as a second language</h1>
      <p class="lead">Proofreading by a native English speaker with an English Honours degree.</p>
      <p class="detail">Includes correct all English language errors, spelling and grammar mistakes, reference checking and editing for style, coherence and clarity.</p>
    </header>

    <div class="brand"><span>Clearpage</span></div>

    <section class="services">
      <h2 class="section-title">We will proofread your:</h2>
      <ul>
        <li>essays &amp; assignments</li>
        <li>theses</li>
        <li>resumes</li>
        <li>business correspondence</li>
        <li>training manuals</li>
        <li>newsletters</li>
        <li>advertising copy</li>
        <li>brochures, catalogues</li>
        <li class="cont">&amp; media releases</li>
        <li>websites</li>
        <li>presentations &amp; speeches</li>
        <li>novels &amp; short stories</li>
      </ul>
    </section>

    <section class="price-guide">
      <h2 class="section-title">Price guide:</h2>
      <p><span class="hl">Prices start at only $20</span><br>(short menus, flyers, letters).</p>
      <p>Discounts for not-for-profit organisations and students.</p>
      <p><span class="hl">Great student discount rate: $25 per hour</span><br><small>(roughly 1000 words - 4 pages - of well-written text).</small></p>
      <p>Package deals on documents over <span class="hl">50,000 words.</span></p>
      <p>Fast, negotiable time-frames<br><small>(same day service available by special arrangement).</small></p>
    </section>

    <div class="desk-photo" role="img" aria-label="Photo of hands working with a book and keyboard on a desk"></div>

    <section class="testimonial">
      <h2 class="section-title">Testimonial:</h2>
      <blockquote>Clara understood our requirements quickly and has been fantastic at delivering quality work, on time and within agreed budget. It's a pleasure to work with her.</blockquote>
      <p class="by"><strong>Ruth Palmer</strong>Operations Manager<br>Tellwave AU</p>
    </section>

    <footer class="footer">Contact us for an obligation free quote: 0400 123 456 / proofing@clearpage.com.au</footer>
  </main>
</body>
</html>
```